Yoga Studio needs a new website

I am looking for someone to design a landing/home page for my website. The website will be developed using Wordpress, so please make sure your designs are compatible.

Please note the following design guidelines about the page:
1. The website is for a yoga studio called “Mirel Yoga”. The logo for our studio has been uploaded on along with this project. Mirel in Sanskrit means Truth and Yoga means unity or unification (with supreme consciousness).
2. The Yoga studio will probably the first of its kinda to offer true, authentic, spiritual experience to students in South Africa. More than that, it aims to setup itself as a hub for spiritualists and seekers irrespective of beliefs, religion and what philosophies they subscribe to.
3. Unlike modern schools, this school focuses on true elements of yoga - and teaches Yoga the way it was meant to be - no westernisation. Must have a peaceful, clam, very clean and spiritual look.
4. Please pay careful attention to the logo, color schemes and the simple design. The site must reflect exactly the same principles.
5. Please use the latest web design trends and ideas in your design. You are free to be as creative as you want.
6. You are free to combine or use design concepts from other philosophies such as Sufism, Bahai, Tantra, Buddhism etc. as long as it gels well with the Yoga theme.
7. The overall site should give a very sensual, feminine and very mystic feel.

Functionality, features and guidelines for the main page design:
1. The main page should give a very clean, expansive, clutter free look.
2. The designer should find a clean way to fit all the following links/information into a main page. First prize if the designer could fit everything in a “single screen” - no scrolling.
3. Visually, the following information must be presented on the main page:
1. The name/logo of the studio.
2. The following sections of the website should have a link on the main page. Sub items represent sub sections within a section.
1. Home - Redirects the user back to home page
2. About
1. Mirel Yoga
2. Instructors
3. FAQ
3. Private Sessions
4. Corporate
1. At Workplace
2. Offisite & Team Building
3. Specialized
5. Retreats
6. Therapy
1. Stress & Anxiety
2. Lifestyle Diseases
3. Rehabilitation
4. Others
7. Gallery
8. Contact Us
3. A Calendar for classes and events
4. A section to display latest blog articles with option to share on social media sites.
5. A separate section to display latest news items.
6. A section for photo gallery - the gallery can be categorised in albums. The main page can display a limited number of images and clicking on the image should take user to our flicker account.
7. Lastly, a nice and clean way to show our activity on various social media streams such as facebook, twitter, flickr, Facebook page, google plus etc.

Please do not limit yourself to the brief above. If you any creative ideas or concepts, please feel free to experiment and suggest new features. Use you full creativity.
Updates

Hi, Thank you for all the designs so far and for your hard work. Just wanted to let you know that you can also include design elements from other philosophies as well if you want to such as Sufism, Bahai, Tantra, Buddhism etc. as long as it gels well with the over all Yoga theme. Please also note that the final design have a mystic, feminine and sensual feel to it. Please also try and include/match the logo styles in the design as well. The site should look very premium, very exclusive - just like the logo.

Target Market(s)

the site is being designed for serious yoga practitioners and learners in the age group of 18-45

Industry/Entity Type

School

Requirements
Must have
• clean, expansive, elegant, simple, calming, soothing, peaceful

```html
<!DOCTYPE html>
<html lang="en">
<head>
<meta charset="utf-8">
<title>Mirel Yoga</title>
<link rel="stylesheet" href="https://fonts.googleapis.com/css2?family=Lato:wght@400;700&family=Open+Sans:wght@400;700&family=Mulish:wght@400;700&display=swap">
<style>
  :root {
    --brand-blue: #2a7fc9;
    --brand-blue-dark: #1d5ea8;
    --text-dark: #2e2e2e;
    --text-body: #3a3a3a;
    --white: #ffffff;
    --nav-bg: rgba(40, 40, 30, 0.28);
    --footer-bg: #2b2b2b;
    --dash: #9bb8d6;
    --fb: #3b5998;
    --tw: #29a9e1;
    --fl: #1a1a1a;
    --gp: #dd4b39;
  }
  * { box-sizing: border-box; margin: 0; padding: 0; }
  html, body { width: 1200px; height: 907px; overflow: hidden; background: var(--white); }
  body { position: relative; font-family: "Mulish", sans-serif; color: var(--text-body); }

  .hero {
    position: absolute; left: 0; top: 0; width: 1200px; height: 551px;
    background:
      radial-gradient(ellipse 260px 360px at 640px 330px, #e9e4dc 0%, rgba(233,228,220,0.85) 40%, rgba(233,228,220,0) 75%),
      radial-gradient(ellipse 520px 220px at 600px 470px, #c9d72a 0%, rgba(201,215,42,0) 80%),
      radial-gradient(ellipse 400px 300px at 200px 200px, #5f5a2a 0%, rgba(95,90,42,0) 80%),
      linear-gradient(180deg, #3e3a22 0%, #6d6a26 35%, #9fae23 65%, #b4c42b 100%);
  }

  .logo {
    position: absolute; left: 129px; top: 2px; width: 156px; height: 156px;
    border-radius: 50%; background: var(--white); border: 4px solid var(--brand-blue);
    display: flex; align-items: center; justify-content: center;
  }
  .logo-name {
    font-family: "Lato", sans-serif; font-weight: 700; font-size: 22px;
    color: var(--brand-blue-dark);
  }

  .main-nav {
    position: absolute; left: 302px; top: 51px; width: 898px; height: 51px;
    background: var(--nav-bg); display: flex; align-items: center;
    font-family: "Lato", sans-serif; font-size: 14px; color: var(--white);
  }
  .main-nav a { position: absolute; color: var(--white); text-decoration: none; transform: translateX(-50%); white-space: nowrap; }
  .main-nav a.is-active {
    left: 0; transform: none; width: 85px; height: 51px; background: var(--brand-blue);
    display: flex; align-items: center; justify-content: center;
  }

  .hero-title {
    position: absolute; left: 133px; top: 278px;
    font-family: "Open Sans", sans-serif; font-weight: 700; font-size: 55px; color: var(--white);
    letter-spacing: 0.5px;
  }
  .hero-tagline {
    position: absolute; left: 135px; top: 346px;
    font-family: "Open Sans", sans-serif; font-size: 16.5px; color: var(--white);
  }

  .hero-thumbs {
    position: absolute; left: 130px; top: 476px; width: 257px; height: 46px;
    display: flex; border: 1px solid rgba(255,255,255,0.8);
  }
  .thumb { flex: 1; border-right: 1px solid rgba(255,255,255,0.7); }
  .thumb:last-child { border-right: 0; }
  .thumb-1 { background: linear-gradient(180deg, #5e6a20, #b6c02c); }
  .thumb-2 { background: linear-gradient(180deg, #8fa2b4, #6a7a86); }
  .thumb-3 { background: linear-gradient(180deg, #a9a59a, #8a8676); }
  .thumb-4 { background: linear-gradient(180deg, #b9c0c6, #8f9a72); }

  .panel {
    position: absolute; top: 551px; height: 321px; padding-top: 43px;
  }
  .panel-about { left: 128px; width: 312px; }
  .panel-blog { left: 443px; width: 322px; padding-left: 16px;
    box-shadow: -8px 0 10px -8px rgba(0,0,0,0.18), 8px 0 10px -8px rgba(0,0,0,0.18); }
  .panel-news { left: 766px; width: 306px; padding-left: 19px; }

  .panel-head { display: flex; align-items: flex-start; height: 52px; }
  .panel-icon { width: 34px; height: 34px; margin-right: 22px; margin-top: 2px; flex: none; }
  .panel-title { font-family: "Lato", sans-serif; font-size: 22px; color: var(--brand-blue); line-height: 1; margin-top: 2px; }
  .panel-sub { font-family: "Mulish", sans-serif; font-weight: 700; font-size: 11px; color: var(--text-dark); margin-top: 9px; }

  .panel-text { font-size: 14px; line-height: 22px; text-align: justify; color: var(--text-body); }
  .panel-about .panel-text { padding-left: 3px; margin-top: 10px; }
  .panel-blog .panel-text { margin-top: 7px; }
  .post-date { font-size: 13px; margin-top: 15px; padding-left: 2px; color: var(--text-dark); }
  .news-item { font-size: 14px; line-height: 22px; padding-bottom: 9px; border-bottom: 1px dashed var(--dash); }
  .news-list { margin-top: 13px; }
  .news-item + .news-item { margin-top: 14px; }

  .read-more {
    position: absolute; top: 256px; width: 105px; height: 32px; border: 1px solid var(--brand-blue);
    border-radius: 3px; font-family: "Lato", sans-serif; font-size: 14px; color: var(--brand-blue);
    display: flex; align-items: center; justify-content: center; text-decoration: none;
  }
  .panel-about .read-more { left: 0; }
  .panel-blog .read-more { left: 19px; }
  .panel-news .read-more { left: 21px; }

  .site-footer {
    position: absolute; left: 0; top: 872px; width: 1200px; height: 35px; background: var(--footer-bg);
  }
  .copyright { position: absolute; left: 130px; top: 11px; font-size: 11px; color: var(--white); }
  .social { position: absolute; left: 975px; top: 7px; display: flex; gap: 4px; }
  .social a { width: 21px; height: 21px; display: block; }
  .social-fb { background: var(--fb); }
  .social-tw { background: var(--tw); }
  .social-fl { background: var(--fl); }
  .social-gp { background: var(--gp); }
</style>
</head>
<body>
  <header class="hero" role="img" aria-label="Photo of a woman meditating cross-legged on sunlit grass in a park">
    <div class="logo"><span class="logo-name">Mirel Yoga</span></div>
    <nav class="main-nav">
      <a class="is-active" href="#">About</a>
      <a href="#" style="left:155px">Private Sessions</a>
      <a href="#" style="left:288px">Corporate</a>
      <a href="#" style="left:398px">Retreats</a>
      <a href="#" style="left:501px">Therapy</a>
      <a href="#" style="left:602px">Gallery</a>
      <a href="#" style="left:713px">Contact Us</a>
    </nav>
    <h1 class="hero-title">Yoga For Truth</h1>
    <p class="hero-tagline">Lorem ipsum dolor sit amet, consecte adipiscing.</p>
    <div class="hero-thumbs">
      <div class="thumb thumb-1" role="img" aria-label="Gallery thumbnail: meditation on grass"></div>
      <div class="thumb thumb-2" role="img" aria-label="Gallery thumbnail: meditation by the water"></div>
      <div class="thumb thumb-3" role="img" aria-label="Gallery thumbnail: seated yoga pose"></div>
      <div class="thumb thumb-4" role="img" aria-label="Gallery thumbnail: meditation outdoors"></div>
    </div>
  </header>

  <section class="panel panel-about">
    <div class="panel-head">
      <svg class="panel-icon" viewBox="0 0 34 34"><circle cx="17" cy="17" r="14" fill="none" stroke="var(--brand-blue)" stroke-width="2"/></svg>
      <div>
        <h2 class="panel-title">About Mirel Yoga</h2>
        <p class="panel-sub">Lorem ipsum dolor sit amet, consectetuer</p>
      </div>
    </div>
    <p class="panel-text">Lorem ipsum dolor sit amet, consectetuer adipiscing elit, sed diam nonummy nibh euismod tincidunt ut laoreet dolore magna aliquam erat volutpat. Ut wisi enim ad minim veniam, quis nostrud exerci tation ullamcorper</p>
    <a class="read-more" href="#">read more</a>
  </section>

  <section class="panel panel-blog">
    <div class="panel-head">
      <svg class="panel-icon" viewBox="0 0 34 34"><circle cx="17" cy="17" r="16" fill="var(--brand-blue)"/></svg>
      <div>
        <h2 class="panel-title">Latest blog</h2>
        <p class="panel-sub">Lorem ipsum dolor sit amet, consectetuer</p>
      </div>
    </div>
    <p class="panel-text">Lorem ipsum dolor sit amet, consectetuer adipiscing elit, sed diam nonummy nibh euismod tincidunt ut laoreet dolore magna aliquam erat volutpat. Ut wisi enim ad minim veniam, quis nostrud exerci tation ullamcorper</p>
    <p class="post-date">29 feb 2014</p>
    <a class="read-more" href="#">read more</a>
  </section>

  <section class="panel panel-news">
    <div class="panel-head">
      <svg class="panel-icon" viewBox="0 0 34 34">
        <circle cx="17" cy="17" r="16" fill="var(--brand-blue)"/>
        <circle cx="17" cy="17" r="12.5" fill="none" stroke="var(--white)" stroke-width="1.5"/>
        <rect x="10" y="11" width="14" height="12" rx="1" fill="var(--white)"/>
        <rect x="12" y="13" width="5" height="4" fill="var(--brand-blue)"/>
        <rect x="18.5" y="13.5" width="4" height="1.2" fill="var(--brand-blue)"/>
        <rect x="18.5" y="16" width="4" height="1.2" fill="var(--brand-blue)"/>
        <rect x="12" y="19" width="10.5" height="1.2" fill="var(--brand-blue)"/>
      </svg>
      <div>
        <h2 class="panel-title">Latest News</h2>
        <p class="panel-sub">Lorem ipsum dolor sit amet, consectetuer</p>
      </div>
    </div>
    <div class="news-list">
      <p class="news-item">Lorem ipsum dolor sit amet, consectetuer adipiscing elit,Lorem ipsum dolor sit amet,</p>
      <p class="news-item">Lorem ipsum dolor sit amet, consectetuer adipiscing elit,Lorem ipsum dolor sit amet,</p>
    </div>
    <a class="read-more" href="#">read more</a>
  </section>

  <footer class="site-footer">
    <p class="copyright">Copyright © 2015&nbsp; Mirel Yoga. All rights reserved.</p>
    <div class="social">
      <a class="social-fb" href="#" aria-label="Social link 1"></a>
      <a class="social-tw" href="#" aria-label="Social link 2"></a>
      <a class="social-fl" href="#" aria-label="Social link 3"></a>
      <a class="social-gp" href="#" aria-label="Social link 4"></a>
    </div>
  </footer>
</body>
</html>
```